Photography Business, Business Card

Looking for a unique cutting edge card that takes advantage of the latest printing technologies. Please review this site for all the options they office: https://plumeprints.example. If you can think it they can do it. And if you have an idea and do not know if they can do it, I will check into it.
Updates

Target Market(s)

People and places I took images of and future clients.

Industry/Entity Type

Photography

Contact Information for Business Card

Name, cell & email. Derek Hollis, dhollis@kmpvisuals.example, 314-782-0946

Colors

Designer to choose only greyscale colors for use in the design.

Requirements
Must have
• 100% cutting edge. Is so great, those I hand it to always show it to someone else. A piece of art.
Nice to have
• Blacks, silvers, greys, some red. Maybe other colors?

```html
<!DOCTYPE html>
<html lang="en">
<head>
<meta charset="utf-8">
<title>KMP Photography – Business Card Alternatives</title>
<link rel="stylesheet" href="https://fonts.googleapis.com/css2?family=Nunito+Sans:ital,wght@0,400;0,600;0,800;1,400&family=Mrs+Saint+Delafield&display=swap">
<style>
  :root{
    --page:#ffffff;
    --text:#1a1a1a;
    --silver:#b3b3b5;
    --silver-soft:#b5b5b7;
    --grey:#888888;
    --grey-dark:#878787;
    --coal:#222222;
    --paper:#ffffff;
    --rule:#cccccc;
  }
  *{margin:0;padding:0;box-sizing:border-box}
  html,body{width:1200px;height:925px;overflow:hidden;background:var(--page)}
  body{position:relative;font-family:"Nunito Sans",Arial,sans-serif;color:var(--text)}
  .board{position:absolute;inset:0;width:1200px;height:925px}
  .alt-label{position:absolute;font-weight:800;font-size:20px;letter-spacing:.2px;color:#000}
  .alt-label.one{left:72px;top:52px}
  .alt-label.two{left:73px;top:468px}
  .alt-label.three{left:834px;top:55px}
  .designer-note{position:absolute;left:804px;top:722px;width:360px;font-size:13.2px;line-height:20.6px;color:var(--text)}

  /* card tones */
  .tone-silver{--film:var(--silver);--edge:none;--hole:var(--paper);--frame:var(--paper);--ink:#111;--side:#222}
  .tone-grey{--film:var(--paper);--edge:var(--rule);--hole:var(--grey);--frame:var(--grey);--ink:#fff;--side:#222}
  .tone-coal{--film:var(--paper);--edge:var(--rule);--hole:var(--coal);--frame:var(--coal);--ink:#fff;--side:#222}
  .tone-steel{--film:var(--grey-dark);--edge:var(--rule);--hole:var(--paper);--frame:var(--paper);--ink:#222;--side:#222}
  .tone-mist{--film:var(--paper);--edge:var(--rule);--hole:var(--silver-soft);--frame:var(--silver-soft);--ink:#222;--side:#222}
  .tone-coal-ink{--film:var(--paper);--edge:var(--rule);--hole:var(--coal);--frame:var(--coal);--ink:#fff;--side:#222}

  .brand{font-family:"Nunito Sans",Arial,sans-serif;font-weight:400}
  .script{font-family:"Mrs Saint Delafield",cursive}
  .contact{font-family:"Nunito Sans",Arial,sans-serif;font-style:italic}
  .edge-note{font-family:"Nunito Sans",Arial,sans-serif;font-weight:600}
</style>
</head>
<body>
<div class="alt-label one">Alt 1</div>
<div class="alt-label two">Alt 2</div>
<div class="alt-label three">Alt 3</div>

<svg class="board" viewBox="0 0 1200 925" xmlns="http://www.w3.org/2000/svg">
  <defs>
    <!-- vertical film card, logo frame on top -->
    <symbol id="card-logo-top" viewBox="0 0 208 330" width="208" height="330">
      <rect x="0.5" y="0.5" width="207" height="329" rx="3" style="fill:var(--film);stroke:var(--edge)"/>
      <line x1="19.5" y1="5.5" x2="19.5" y2="325" stroke-width="17" stroke-dasharray="12 8.5" style="stroke:var(--hole)"/>
      <line x1="188.5" y1="5.5" x2="188.5" y2="325" stroke-width="17" stroke-dasharray="12 8.5" style="stroke:var(--hole)"/>
      <rect x="32" y="5.5" width="144" height="157.5" rx="7" style="fill:var(--frame)"/>
      <rect x="32" y="168" width="144" height="157" rx="7" style="fill:var(--frame)"/>
      <text x="104" y="80" text-anchor="middle" class="brand" font-size="30" letter-spacing="5" style="fill:var(--ink)">KMP</text>
      <text x="104" y="101" text-anchor="middle" class="brand" font-size="10.5" style="fill:var(--ink)">Photography</text>
      <text x="104" y="232" text-anchor="middle" class="script" font-size="34" style="fill:var(--ink)">Derek Hollis</text>
      <text x="104" y="262" text-anchor="middle" class="contact" font-size="9.5" style="fill:var(--ink)">dhollis@kmpvisuals.example</text>
      <text x="104" y="279" text-anchor="middle" class="contact" font-size="10" style="fill:var(--ink)">314-782-0946</text>
      <text class="edge-note" font-size="5.6" transform="translate(200 20) rotate(90)" style="fill:var(--side)">Derek Hollis</text>
      <text class="edge-note" font-size="5.6" transform="translate(200 254) rotate(90)" style="fill:var(--side)">KMP Photography</text>
      <text class="edge-note" font-size="5.6" transform="translate(5 100) rotate(90)" style="fill:var(--side)">25</text>
      <text class="edge-note" font-size="5.6" transform="translate(5 202) rotate(90)" style="fill:var(--side)">26</text>
      <path d="M2.5 318 L5.5 313 L8.5 318 Z" style="fill:var(--side)"/>
    </symbol>

    <!-- vertical film card, name frame on top -->
    <symbol id="card-name-top" viewBox="0 0 208 331" width="208" height="331">
      <rect x="0.5" y="0.5" width="207" height="330" rx="3" style="fill:var(--film);stroke:var(--edge)"/>
      <line x1="20.5" y1="5.5" x2="20.5" y2="326" stroke-width="17" stroke-dasharray="12 8.5" style="stroke:var(--hole)"/>
      <line x1="188.5" y1="5.5" x2="188.5" y2="326" stroke-width="17" stroke-dasharray="12 8.5" style="stroke:var(--hole)"/>
      <path d="M32 0.5 H177 V22 a7 7 0 0 1 -7 7 H39 a7 7 0 0 1 -7 -7 Z" style="fill:var(--frame)"/>
      <rect x="32" y="36" width="145" height="127.5" rx="7" style="fill:var(--frame)"/>
      <rect x="32" y="169" width="145" height="128" rx="7" style="fill:var(--frame)"/>
      <path d="M32 330.5 H177 V309 a7 7 0 0 0 -7 -7 H39 a7 7 0 0 0 -7 7 Z" style="fill:var(--frame)"/>
      <text x="104.5" y="89" text-anchor="middle" class="script" font-size="34" style="fill:var(--ink)">Derek Hollis</text>
      <text x="104.5" y="117" text-anchor="middle" class="contact" font-size="9.5" style="fill:var(--ink)">dhollis@kmpvisuals.example</text>
      <text x="104.5" y="135" text-anchor="middle" class="contact" font-size="10" style="fill:var(--ink)">314-782-0946</text>
      <text x="104.5" y="226" text-anchor="middle" class="brand" font-size="30" letter-spacing="5" style="fill:var(--ink)">KMP</text>
      <text x="104.5" y="247" text-anchor="middle" class="brand" font-size="10.5" style="fill:var(--ink)">Photography</text>
      <text class="edge-note" font-size="5.6" transform="translate(200 20) rotate(90)" style="fill:var(--side)">Derek Hollis</text>
      <text class="edge-note" font-size="5.6" transform="translate(200 254) rotate(90)" style="fill:var(--side)">KMP Photography</text>
      <text class="edge-note" font-size="5.6" transform="translate(5 100) rotate(90)" style="fill:var(--side)">25</text>
      <text class="edge-note" font-size="5.6" transform="translate(5 204) rotate(90)" style="fill:var(--side)">26</text>
      <path d="M3 320 L6 315 L9 320 Z" style="fill:var(--side)"/>
    </symbol>

    <!-- horizontal film card -->
    <symbol id="card-wide" viewBox="0 0 291 182" width="291" height="182">
      <rect x="0.5" y="0.5" width="290" height="181" rx="3" style="fill:var(--film);stroke:var(--edge)"/>
      <line x1="19.5" y1="6" x2="19.5" y2="178" stroke-width="15" stroke-dasharray="11 6.8" style="stroke:var(--hole)"/>
      <line x1="271.5" y1="6" x2="271.5" y2="178" stroke-width="15" stroke-dasharray="11 6.8" style="stroke:var(--hole)"/>
      <path d="M33 0 H258 V66 a4 4 0 0 1 -4 4 H37 a4 4 0 0 1 -4 -4 Z" style="fill:var(--frame)"/>
      <rect x="33" y="76.5" width="225" height="100.5" rx="4" style="fill:var(--frame)"/>
      <text x="145.5" y="37" text-anchor="middle" class="brand" font-size="22" letter-spacing="4" style="fill:var(--ink)">KMP</text>
      <text x="145.5" y="50" text-anchor="middle" class="brand" font-size="7.5" style="fill:var(--ink)">Photography</text>
      <text x="145.5" y="126" text-anchor="middle" class="script" font-size="38" style="fill:var(--ink)">Derek Hollis</text>
      <text x="145.5" y="149" text-anchor="middle" class="contact" font-size="9.5" style="fill:var(--ink)">dhollis@kmpvisuals.example</text>
      <text x="145.5" y="164" text-anchor="middle" class="contact" font-size="9.5" style="fill:var(--ink)">314-782-0946</text>
      <text class="edge-note" font-size="5" transform="translate(283 8) rotate(90)" style="fill:var(--side)">Derek Hollis</text>
      <text class="edge-note" font-size="5" transform="translate(283 124) rotate(90)" style="fill:var(--side)">KMP Photography</text>
      <text class="edge-note" font-size="5" transform="translate(5 6) rotate(90)" style="fill:var(--side)">25</text>
      <text class="edge-note" font-size="5" transform="translate(5 97) rotate(90)" style="fill:var(--side)">26</text>
      <path d="M4 176 L6.5 172 L9 176 Z" style="fill:var(--side)"/>
    </symbol>
  </defs>

  <!-- Alt 1 -->
  <g class="alt-one">
    <use href="#card-logo-top" x="72" y="90" class="tone-silver"/>
    <use href="#card-logo-top" x="298" y="90" class="tone-grey"/>
    <use href="#card-logo-top" x="518" y="90" class="tone-coal"/>
  </g>

  <!-- Alt 2 -->
  <g class="alt-two">
    <use href="#card-name-top" x="76" y="502" class="tone-steel"/>
    <use href="#card-name-top" x="302" y="502" class="tone-mist"/>
    <use href="#card-name-top" x="522" y="502" class="tone-coal-ink"/>
  </g>

  <!-- Alt 3 -->
  <g class="alt-three">
    <use href="#card-wide" x="834" y="97" class="tone-silver"/>
    <use href="#card-wide" x="834" y="293" class="tone-grey"/>
    <use href="#card-wide" x="834" y="488" class="tone-coal"/>
  </g>
</svg>

<p class="designer-note">Hi Mr. Hollis<br>
Thank you for your time for this revision.<br>
Here are some alternatives based on your feedback. I’d like to recommend the edges a bit round for safetiness.<br>
I made the edges to look neither too round or sharp.<br>
If you have any feedback please reach me out. Thank you and have a good day!</p>
</body>
</html>
```